Company Profile for Consulting Comany

Need Company profile to be designed in a professional way.

for inspiring :-
https://www.vimolia.net/gallery/5307462/COMPANY-PROFILE
https://www.vimolia.net/gallery/20934617/Biotech-Product-Catalog-No1-(Laminar-Air-Flow)
https://www.vimolia.net/gallery/38720954/RKT-Tramvale-Company-Profile-2014-(RKT-Rebrand-part-2)

Target Market(s)

Corporate

Industry/Entity Type

It Company

Font styles to use
Sans Serif

Requirements
Must have
• Landscape A4 size
• Must go with the logo branding
• Must Have Visual Identity is the most important
• Must Have mpty spaces

```html
<!DOCTYPE html>
<html lang="en">
<head>
<meta charset="utf-8">
<title>Movera Consulting – Company Profile</title>
<link href="https://fonts.googleapis.com/css2?family=Open+Sans:wght@400;600;700;800&family=Oswald:wght@500;700&display=swap" rel="stylesheet">
<style>
  :root{
    --bg:#b5b6b8;
    --paper:#ffffff;
    --ink:#1d1f22;
    --grey-text:#55595e;
    --blue:#1597c9;
    --cyan:#3cc6ec;
    --deep:#0b5f86;
    --night:#0c0d0f;
    --mist:#cfe6ef;
  }
  *{box-sizing:border-box;margin:0;padding:0}
  html,body{width:1000px;height:1200px;overflow:hidden}
  body{background:var(--bg);font-family:"Open Sans",Arial,sans-serif;color:var(--ink);position:relative}

  .piece{position:absolute;overflow:hidden;background:var(--paper)}
  .band{position:absolute;left:0;right:0;bottom:0;width:100%}
  .photo{position:absolute}

  /* Brand name used in place of logo */
  .brand{display:flex;align-items:center;gap:8px;color:var(--blue);font-family:"Open Sans",Arial,sans-serif;font-weight:700;line-height:1}
  .brand-mark{background:var(--blue);flex:none}

  /* Front cover */
  .cover{left:150px;top:40px;width:700px;height:420px;background:var(--night)}
  .cover .photo{left:0;top:0;width:100%;height:300px;background:linear-gradient(180deg,#8c8c8c 0%,#5a5a5a 35%,#2a2a2a 70%,#0c0d0f 100%)}
  .cover-lead{position:absolute;top:48px;width:100%;text-align:center;color:#fff;font-weight:600;font-size:26px;letter-spacing:7px}
  .cover-title{position:absolute;top:84px;width:100%;text-align:center;color:#fff;font-weight:800;font-size:46px;letter-spacing:1px}
  .cover .brand{position:absolute;left:190px;top:250px;font-size:44px}
  .cover .brand-mark{width:40px;height:40px}
  .cover-kicker{position:absolute;left:420px;top:240px;color:var(--blue);font-size:11px;letter-spacing:3px;font-weight:600}
  .cover-tagline{position:absolute;left:240px;top:302px;color:#8a8f94;font-size:15px;letter-spacing:2px}

  /* Back cover */
  .back{left:590px;top:520px;width:340px;height:240px;background:var(--night)}
  .back .photo{left:0;top:20px;width:100%;height:110px;background:radial-gradient(ellipse at 50% 80%,#d8d8d8 0%,#6d6d6d 25%,#1b1b1b 65%,#0c0d0f 100%)}
  .back .brand{position:absolute;left:92px;top:140px;font-size:24px}
  .back .brand-mark{width:22px;height:22px}
  .back-tagline{position:absolute;left:122px;top:168px;color:#8a8f94;font-size:8px;letter-spacing:1px}

  /* Spreads */
  .spread{width:470px;height:166px}
  .spread .page{position:absolute;top:0;width:50%;height:100%}
  .spread .page.left{left:0}
  .spread .page.right{left:50%}
  .spread .fold{position:absolute;left:50%;top:0;width:2px;height:100%;background:linear-gradient(90deg,rgba(0,0,0,.08),rgba(255,255,255,0))}
  .spread .footer-url{position:absolute;bottom:4px;color:#fff;font-size:4.5px;font-weight:600}
  .spread .footer-mark{position:absolute;bottom:3px;width:7px;height:7px;background:#fff}

  .heading{position:absolute;display:flex;align-items:baseline;font-family:"Oswald",Arial,sans-serif;font-weight:700;text-transform:uppercase;color:var(--ink);line-height:1}
  .heading::before{content:"";width:2px;align-self:stretch;background:var(--blue);margin-right:4px}
  .heading .accent{color:var(--blue)}
  .heading .echo{color:#e4e6e8}

  .copy{position:absolute;font-size:4.6px;line-height:1.45;color:var(--grey-text)}
  .copy b{color:var(--ink)}
  .copy .key{color:var(--blue);font-weight:700}
  .copy p{margin-bottom:3px}

  .toc{left:20px;top:530px}
  .toc .photo{left:50%;top:0;width:50%;height:150px;background:linear-gradient(135deg,#e8f3f7 0%,#9fcadb 45%,#4c98b8 100%)}
  .toc .brand{position:absolute;right:12px;top:10px;font-size:10px;color:var(--deep)}
  .toc .brand-mark{width:9px;height:9px;background:var(--deep)}
  .toc .heading{left:14px;top:100px;font-size:20px;flex-direction:column;align-items:flex-start}
  .toc .heading::before{display:none}
  .toc-bar{position:absolute;left:10px;top:98px;width:2px;height:42px;background:var(--blue)}
  .toc-list{position:absolute;left:90px;top:20px;font-size:5px;line-height:1.5;font-weight:700;color:var(--blue);list-style:none}
  .toc-list li.sub{color:var(--ink);font-weight:600;padding-left:6px}

  .who{left:15px;top:810px}
  .who .photo{left:34%;top:0;width:66%;height:150px;background:linear-gradient(120deg,#f2f7fa 0%,#bcd9e6 35%,#4f8fb0 70%,#1f5c7d 100%)}
  .who .heading{left:12px;top:34px;font-size:15px}
  .who .copy{left:12px;top:58px;width:165px}

  .why{left:515px;top:810px}
  .why .photo{left:0;top:0;width:100%;height:150px;background:linear-gradient(180deg,#ffffff 0%,#e9f2f6 45%,#a9c9d8 80%,#6b9db5 100%)}
  .why .photo.cliff{left:auto;right:0;width:70px;background:linear-gradient(180deg,#5c7d8e,#2b4656)}
  .why .heading{left:12px;top:20px;font-size:15px}
  .why .copy{left:12px;top:42px;width:300px}

  .vision{left:15px;top:1010px}
  .vision .photo.stones{left:120px;top:0;width:115px;height:150px;background:linear-gradient(180deg,#ffffff 0%,#dde9ee 40%,#a9c4d1 100%)}
  .vision .photo.pier{left:50%;top:0;width:50%;height:150px;background:linear-gradient(180deg,#eef6f9 0%,#b6d6e4 55%,#5e97b1 100%)}
  .vision .h-vision{left:10px;top:20px;font-size:12px}
  .vision .h-mission{left:10px;top:70px;font-size:12px}
  .vision .h-values{left:248px;top:42px;font-size:14px}
  .vision .c-vision{left:10px;top:40px;width:105px}
  .vision .c-mission{left:10px;top:90px;width:60px}
  .vision .c-mission-list{left:74px;top:90px;width:70px}
  .vision .c-values{left:248px;top:62px;width:140px}
  .vision .brand{position:absolute;left:400px;top:34px;font-size:9px}
  .vision .brand-mark{width:8px;height:8px}

  .partners{left:515px;top:1010px}
  .partners .photo{left:0;top:0;width:55%;height:150px;background:linear-gradient(110deg,#3b5d70 0%,#9fbfcd 45%,#e3eef3 100%)}
  .partners .heading{left:258px;top:14px;font-size:13px}
  .partner-badge{position:absolute;width:38px;height:12px;background:var(--deep)}
  .partner-badge.soft{background:#c98aa8}
  .partner-badge.grey{background:#7c8287}
  .partner-badge.orange{background:#e38a2e}
  .partners .copy{width:60px;font-size:3.8px}
</style>
</head>
<body>

<!-- Front cover -->
<section class="piece cover" aria-label="Front cover">
  <div class="photo" role="img" aria-label="Black and white photo of a misty forest seen from below, tall tree trunks reaching upward"></div>
  <p class="cover-lead">WE CAN HELP YOU TO</p>
  <h1 class="cover-title">MAKE CHANGE HAPPEN</h1>
  <span class="cover-kicker">CONSULTING</span>
  <div class="brand"><span class="brand-mark"></span>Movera</div>
  <p class="cover-tagline">A Move Towards Change</p>
  <svg class="band" viewBox="0 0 700 60" height="60" preserveAspectRatio="none" aria-hidden="true">
    <defs>
      <linearGradient id="coverBand" x1="0" x2="1">
        <stop offset="0" stop-color="#0b5f86"/><stop offset=".5" stop-color="#3cc6ec"/><stop offset="1" stop-color="#1597c9"/>
      </linearGradient>
    </defs>
    <path d="M0 30 C180 10 420 38 700 14 L700 60 L0 60 Z" fill="url(#coverBand)"/>
    <path d="M0 36 C220 18 440 44 700 22" stroke="#bfefff" stroke-width="1.5" fill="none" opacity=".7"/>
  </svg>
</section>

<!-- Table of contents spread -->
<section class="piece spread toc" aria-label="Table of contents spread">
  <div class="page left"></div>
  <div class="photo" role="img" aria-label="Photo of white computer keyboard keys in soft blue light"></div>
  <div class="brand"><span class="brand-mark"></span>Movera</div>
  <span class="toc-bar"></span>
  <h2 class="heading"><span>Table of</span><span>Contents</span></h2>
  <ul class="toc-list">
    <li>WHO WE ARE?</li>
    <li class="sub">EXECUTIVE SUMMARY</li>
    <li class="sub">VISION</li>
    <li class="sub">MISSION</li>
    <li class="sub">VALUES</li>
    <li>WHY MOVERA?</li>
    <li>WHAT WE DO?</li>
    <li class="sub">HR CONSULTING</li>
    <li class="sub">TALENT DEVELOPMENT</li>
    <li class="sub">OUTSOURCING</li>
    <li>PARTNERS</li>
    <li>OUR CLIENTS</li>
    <li class="sub">CONTACT US</li>
  </ul>
  <span class="fold"></span>
  <svg class="band" viewBox="0 0 470 20" height="16" preserveAspectRatio="none" aria-hidden="true">
    <path d="M0 8 C120 2 330 12 470 4 L470 20 L0 20 Z" fill="#1597c9"/>
    <path d="M0 10 C140 4 330 14 470 6" stroke="#3cc6ec" stroke-width="1.2" fill="none"/>
  </svg>
  <span class="footer-url" style="left:90px">www.movera-consult.com</span>
  <span class="footer-url" style="left:300px">www.movera-consult.com</span>
  <span class="footer-mark" style="left:12px"></span>
  <span class="footer-mark" style="right:12px"></span>
</section>

<!-- Back cover -->
<section class="piece back" aria-label="Back cover">
  <div class="photo" role="img" aria-label="Black and white photo of reeds silhouetted against a glowing sunset over water"></div>
  <div class="brand"><span class="brand-mark"></span>Movera</div>
  <p class="back-tagline">A Move Towards Change</p>
  <svg class="band" viewBox="0 0 340 36" height="36" preserveAspectRatio="none" aria-hidden="true">
    <path d="M0 16 C90 6 220 22 340 8 L340 36 L0 36 Z" fill="#1597c9"/>
    <path d="M0 20 C100 10 220 26 340 12" stroke="#bfefff" stroke-width="1" fill="none" opacity=".7"/>
  </svg>
</section>

<!-- Who we are spread -->
<section class="piece spread who" aria-label="Who we are spread">
  <div class="photo" role="img" aria-label="Photo of an empty boardroom with leather chairs around a table, tinted blue"></div>
  <h2 class="heading">Who we are<span class="echo">re</span></h2>
  <div class="copy">
    <p><b>EXECUTIVE SUMMARY</b></p>
    <p>Movera is a professional HR &amp; OD organization specialized in talent and organizational development, career coaching, leadership assessment and payroll services. We help companies across the region grow their people, build stronger teams and plan for the future. Our advisors bring global experience and local knowledge, and we work as one team with each client to find the right answer. We aim to be the strategic partner that provides HR services through smart platforms.</p>
  </div>
  <span class="fold"></span>
  <svg class="band" viewBox="0 0 470 20" height="16" preserveAspectRatio="none" aria-hidden="true">
    <path d="M0 8 C120 2 330 12 470 4 L470 20 L0 20 Z" fill="#1597c9"/>
    <path d="M0 10 C140 4 330 14 470 6" stroke="#3cc6ec" stroke-width="1.2" fill="none"/>
  </svg>
  <span class="footer-url" style="left:90px">www.movera-consult.com</span>
  <span class="footer-url" style="left:300px">www.movera-consult.com</span>
  <span class="footer-mark" style="left:12px"></span>
  <span class="footer-mark" style="right:12px"></span>
</section>

<!-- Why spread -->
<section class="piece spread why" aria-label="Why Movera spread">
  <div class="photo" role="img" aria-label="Pale blue photo of a misty mountain range across both pages"></div>
  <div class="photo cliff" role="img" aria-label="Photo of a climber scaling a rock overhang"></div>
  <h2 class="heading">Why <span class="accent">&nbsp;Movera?</span><span class="echo">s?</span></h2>
  <div class="copy">
    <p><span class="key">SUCCESS</span> We deliver reliable results for you, as our record shows; we have helped many organizations reach their goals this past year.</p>
    <p><span class="key">TARGETING</span> We understand the importance of finding the right people and community. We work with you to learn your needs so you can focus on the right person at the right time.</p>
    <p><span class="key">SUPERIOR WORKFORCE</span> Our dedicated training professionals are screened and trained to perform at the peak level, and they represent our company at all times.</p>
    <p><span class="key">FLEXIBLE WORKFORCE</span> Our wide capabilities give an extensive reach and the ability to create the right program and deliver it where it fits best.</p>
    <p><span class="key">COST EFFECTIVENESS</span> We train your staff by offering very affordable value added projects.</p>
  </div>
  <span class="fold"></span>
  <svg class="band" viewBox="0 0 470 20" height="16" preserveAspectRatio="none" aria-hidden="true">
    <path d="M0 8 C120 2 330 12 470 4 L470 20 L0 20 Z" fill="#1597c9"/>
    <path d="M0 10 C140 4 330 14 470 6" stroke="#3cc6ec" stroke-width="1.2" fill="none"/>
  </svg>
  <span class="footer-url" style="left:90px">www.movera-consult.com</span>
  <span class="footer-url" style="left:300px">www.movera-consult.com</span>
  <span class="footer-mark" style="left:12px"></span>
  <span class="footer-mark" style="right:12px"></span>
</section>

<!-- Vision, mission, values spread -->
<section class="piece spread vision" aria-label="Vision, mission and values spread">
  <div class="photo stones" role="img" aria-label="Photo of a balanced stack of smooth pebbles"></div>
  <div class="photo pier" role="img" aria-label="Photo of a wooden pier leading out over calm blue water"></div>
  <h2 class="heading h-vision">Vision</h2>
  <div class="copy c-vision"><p>"To become the leading HR outsourcing company in the region and stand known for quality services."</p></div>
  <h2 class="heading h-mission">Mission</h2>
  <div class="copy c-mission"><p>We have a clear mission focused on the needs of our customers, adding value to their business and raising our standing.</p></div>
  <div class="copy c-mission-list">
    <p>• To provide convenient HR solutions so firms can focus on their core work.</p>
    <p>• To play our role in growth of the region.</p>
    <p>• To build lasting ties with clients.</p>
  </div>
  <div class="brand"><span class="brand-mark"></span>Movera</div>
  <h2 class="heading h-values">Values<span class="echo">s</span></h2>
  <div class="copy c-values">
    <p><span class="key">• INTEGRITY:</span> Movera acts with integrity with staff, clients and partners.</p>
    <p><span class="key">• WORKPLACE:</span> We promote the enjoyment of all staff at work.</p>
    <p><span class="key">• ACCOUNTABILITY:</span> Each of us owns our actions and decisions.</p>
    <p><span class="key">• PURSUIT OF EXCELLENCE:</span> We strive for the best in every role.</p>
    <p><span class="key">• QUALITY CONTROL:</span> We check and improve our services.</p>
    <p><span class="key">• AFFORDABILITY:</span> Our services meet local budgets.</p>
  </div>
  <span class="fold"></span>
  <svg class="band" viewBox="0 0 470 20" height="16" preserveAspectRatio="none" aria-hidden="true">
    <path d="M0 8 C120 2 330 12 470 4 L470 20 L0 20 Z" fill="#1597c9"/>
    <path d="M0 10 C140 4 330 14 470 6" stroke="#3cc6ec" stroke-width="1.2" fill="none"/>
  </svg>
  <span class="footer-url" style="left:90px">www.movera-consult.com</span>
  <span class="footer-url" style="left:300px">www.movera-consult.com</span>
  <span class="footer-mark" style="left:12px"></span>
  <span class="footer-mark" style="right:12px"></span>
</section>

<!-- Success partnership spread -->
<section class="piece spread partners" aria-label="Success partnership spread">
  <div class="photo" role="img" aria-label="Photo of two business people shaking hands, tinted blue"></div>
  <h2 class="heading">Success <span class="accent">&nbsp;Partnership</span><span class="echo">p</span></h2>
  <span class="partner-badge" style="left:262px;top:38px"></span>
  <span class="partner-badge soft" style="left:370px;top:38px"></span>
  <div class="copy" style="left:262px;top:56px"><p><b>NORVEL</b></p><p>Norvel offers management training and certified programs for leaders.</p></div>
  <div class="copy" style="left:370px;top:56px"><p><b>HALDEN PARTNERS</b></p><p>Halden gives talent advice and coaching to growing teams.</p></div>
  <span class="partner-badge grey" style="left:262px;top:92px"></span>
  <span class="partner-badge orange" style="left:370px;top:92px"></span>
  <div class="copy" style="left:262px;top:108px"><p><b>LUMBROOK</b></p><p>Lumbrook builds digital tools for HR and payroll.</p></div>
  <div class="copy" style="left:370px;top:108px"><p><b>TESSARO</b></p><p>Tessaro runs research and learning for firms.</p></div>
  <span class="fold"></span>
  <svg class="band" viewBox="0 0 470 20" height="16" preserveAspectRatio="none" aria-hidden="true">
    <path d="M0 8 C120 2 330 12 470 4 L470 20 L0 20 Z" fill="#1597c9"/>
    <path d="M0 10 C140 4 330 14 470 6" stroke="#3cc6ec" stroke-width="1.2" fill="none"/>
  </svg>
  <span class="footer-url" style="left:90px">www.movera-consult.com</span>
  <span class="footer-url" style="left:300px">www.movera-consult.com</span>
  <span class="footer-mark" style="left:12px"></span>
  <span class="footer-mark" style="right:12px"></span>
</section>

</body>
</html>
```